Need a design for Loan Site with new age design

We need a design for our site www.fernpivot.in , we deal with different verticals like home loan, personal loan, loan against property and business loans. Feel free to get in touch if you have any questions.

I have like the concept of the drop down on the eye level where consumer is able to select the product they wish and continue with the form https://www.tallowcrest.com/ . They are in the same line of business as we are.

Here are few more designs which i personally like just to get idea about the taste

https://plumweatherly.com/
http://vexlar.com/partners

Industry/Entity Type

Loan

Number of Pages Required

2 page

Colors
34a7d7
add136
faa54b
fbee3e

Requirements
Must have
• I have like the concept of the drop down on the eye level where consumer is able to select the product they wish and continue with the form https://www.tallowcrest.com/ . They are in the same line of business as we are.
• Here are few more designs which i personally like just to get idea about the taste
• https://plumweatherly.com/
• http://vexlar.com/partners

```html
<!DOCTYPE html>
<html lang="en">
<head>
<meta charset="utf-8">
<title>Fern Pivot – Secured and Unsecured Loans</title>
<link href="https://fonts.googleapis.com/css2?family=Open+Sans:wght@400;600;700&family=Raleway:wght@400;500;600&display=swap" rel="stylesheet">
<style>
  :root{
    --brand-blue:#34a7d7;
    --brand-blue-dark:#2a8fc4;
    --navy:#1d3c5a;
    --ink:#333;
    --muted:#666;
    --page-grey:#ececec;
    --white:#fff;
    --hero-top:#55687a;
    --hero-bottom:#2e4254;
    --banner-top:#3a9ee0;
    --banner-bottom:#1f7cc4;
    --footer:#e2e2e2;
    --partner-red:#c0272d;
    --partner-navy:#1f3f7a;
  }
  *{box-sizing:border-box;margin:0;padding:0}
  html,body{width:791px;height:1200px;overflow:hidden}
  body{font-family:'Open Sans',sans-serif;color:var(--ink);background:var(--page-grey);position:relative}

  .site-header{position:absolute;top:0;left:0;width:791px;height:74px;background:var(--white);display:flex;align-items:center;padding:0 40px;justify-content:space-between;z-index:3}
  .brand{display:flex;align-items:center;gap:10px;font-family:'Raleway',sans-serif;font-weight:600;font-size:20px;color:var(--brand-blue-dark)}
  .brand-mark{width:30px;height:30px;background:var(--brand-blue-dark)}
  .main-nav{display:flex;gap:26px;font-size:11px;font-weight:600;color:#555;letter-spacing:.3px}
  .main-nav a{color:inherit;text-decoration:none;padding:28px 0 26px;position:relative}
  .main-nav a.is-active{color:var(--ink)}
  .main-nav a.is-active::after{content:"";position:absolute;left:-6px;right:-6px;bottom:18px;height:2px;background:var(--brand-blue)}

  .hero{position:absolute;top:74px;left:0;width:791px;height:335px;background:linear-gradient(180deg,var(--hero-top),var(--hero-bottom));text-align:center;color:var(--white)}
  .hero-title{font-family:'Raleway',sans-serif;font-weight:600;font-size:27px;margin-top:44px}
  .hero-sub{font-size:17px;margin-top:8px;color:#e6eef5}
  .loan-finder{display:flex;width:424px;height:42px;margin:40px auto 0}
  .loan-finder .select{flex:1;background:var(--white);color:#777;font-size:10px;display:flex;align-items:center;justify-content:center;gap:8px;border-right:1px solid #ddd}
  .loan-finder .select::after{content:"";width:5px;height:5px;border-right:1px solid #888;border-bottom:1px solid #888;transform:rotate(45deg);margin-top:-3px}
  .loan-finder .search-btn{width:104px;background:var(--brand-blue);color:var(--white);font-size:17px;font-weight:600;display:flex;align-items:center;justify-content:center;border:0}

  .partners{position:absolute;top:382px;left:40px;width:711px;height:127px;background:var(--white);box-shadow:0 2px 6px rgba(0,0,0,.15);text-align:center;z-index:2}
  .partners h2{font-family:'Raleway',sans-serif;font-weight:500;font-size:18px;color:var(--ink);margin-top:20px}
  .partner-row{display:flex;justify-content:center;gap:12px;margin-top:16px}
  .partner{width:126px;height:50px;border:1px solid #ddd;display:flex;align-items:center;justify-content:center;font-size:11px;font-weight:700}
  .partner.red{color:var(--partner-red)}
  .partner.navy{color:var(--partner-navy)}

  .features{position:absolute;top:509px;left:0;width:791px;height:374px;text-align:center}
  .features h2{font-family:'Raleway',sans-serif;font-weight:400;font-size:32px;color:#444;margin-top:56px}
  .feature-row{display:flex;justify-content:center;gap:18px;margin-top:26px}
  .feature-card{width:158px;height:200px;background:var(--white);position:relative}
  .feature-photo{height:90px;background:linear-gradient(135deg,#b9b3a8,#6e6a63)}
  .feature-icon{position:absolute;left:50%;top:68px;transform:translateX(-50%);width:46px;height:46px;border-radius:50%;background:var(--brand-blue-dark);border:3px solid var(--white);display:flex;align-items:center;justify-content:center;color:var(--white);font-size:20px;font-weight:700}
  .feature-card p{font-size:11.5px;color:#333;margin:36px 10px 0;line-height:1.35}

  .cta-banner{position:absolute;top:883px;left:0;width:791px;height:277px;background:linear-gradient(180deg,var(--banner-top),var(--banner-bottom));text-align:center;color:var(--white)}
  .cta-art{width:700px;height:150px;margin:14px auto 0;background:radial-gradient(ellipse at center,rgba(255,255,255,.35),rgba(255,255,255,0) 70%)}
  .cta-banner h2{font-family:'Raleway',sans-serif;font-weight:600;font-size:24px;margin-top:0}
  .cta-btn{display:inline-block;margin-top:14px;width:122px;height:37px;line-height:37px;background:var(--navy);color:var(--white);font-size:13px;font-weight:600}

  .site-footer{position:absolute;top:1160px;left:0;width:791px;height:40px;background:var(--footer);font-size:9px;color:#666;display:flex;align-items:center;justify-content:center}
</style>
</head>
<body>
  <header class="site-header">
    <div class="brand"><span class="brand-mark"></span>Fern Pivot</div>
    <nav class="main-nav">
      <a class="is-active" href="#">HOME</a>
      <a href="#">WHO WE ARE</a>
      <a href="#">SERVICES</a>
      <a href="#">BLOG</a>
      <a href="#">CAREER</a>
      <a href="#">REACH US</a>
    </nav>
  </header>

  <section class="hero" role="img" aria-label="Photo of a person signing loan papers at a desk">
    <h1 class="hero-title">Looking for a Secured or Unsecured loan</h1>
    <p class="hero-sub">We will help you Best Interest Rate</p>
    <div class="loan-finder">
      <div class="select">I would like to</div>
      <div class="select">Select a Product</div>
      <button class="search-btn">Search</button>
    </div>
  </section>

  <section class="partners">
    <h2>We work with all premium financial institution</h2>
    <div class="partner-row">
      <div class="partner red">Tessaly Bank</div>
      <div class="partner red">Orvane Bank</div>
      <div class="partner red">Quillmar Bank</div>
      <div class="partner navy">Brennow Finserv</div>
      <div class="partner navy">Halvrek</div>
    </div>
  </section>

  <section class="features">
    <h2>Our Features</h2>
    <div class="feature-row">
      <div class="feature-card">
        <div class="feature-photo" role="img" aria-label="Photo of a smiling couple"></div>
        <div class="feature-icon">
          <svg width="20" height="20" viewBox="0 0 20 20" fill="#fff"><path d="M2 9h3v9H2zM7 9l4-7c1.5 0 2 1 1.7 2.5L12 8h5c1 0 1.6 1 1.3 2l-1.8 6.5c-.3.9-1 1.5-2 1.5H7z"/></svg>
        </div>
        <p>Get approval within<br>7 business days</p>
      </div>
      <div class="feature-card">
        <div class="feature-photo" role="img" aria-label="Photo of a doorstep service"></div>
        <div class="feature-icon">₹</div>
        <p>Doorstep<br>deliveries</p>
      </div>
      <div class="feature-card">
        <div class="feature-photo" role="img" aria-label="Photo of advisors comparing quotes"></div>
        <div class="feature-icon">
          <svg width="22" height="18" viewBox="0 0 22 18" fill="#fff"><path d="M1 3h12v10H1zM14 6h4l3 4v3h-7z"/><circle cx="5" cy="14.5" r="2"/><circle cx="17" cy="14.5" r="2"/></svg>
        </div>
        <p>Compare quote from<br>all major financial<br>institutions</p>
      </div>
      <div class="feature-card">
        <div class="feature-photo" role="img" aria-label="Photo of documents on a desk"></div>
        <div class="feature-icon">
          <svg width="16" height="20" viewBox="0 0 16 20"><path d="M1 1h9l5 5v13H1z" fill="#fff"/><path d="M4 9h8M4 12h8M4 15h6" stroke="#2a8fc4" stroke-width="1.4"/></svg>
        </div>
        <p>Easy<br>Documentation</p>
      </div>
    </div>
  </section>

  <section class="cta-banner">
    <div class="cta-art" role="img" aria-label="Illustration of hands holding a phone with media icons flowing to a cloud"></div>
    <h2>What are you waiting for?</h2>
    <a class="cta-btn">Inquire Now</a>
  </section>

  <footer class="site-footer">Copyright © 2014 Fern Pivot Private Policy. All Right Reserved</footer>
</body>
</html>
```